Flyer Design Project

I provide workshops for teachers, students and parents on organization - specifically laying out 3 goals, their accompanying activities and actions in 3 three hour sessions.

Please go to my website to see my brain logo. I need a flyer with the information typed below. The information may be changed and/or added to in way you see fit to better communicate the organizational intent.This is not for speech therapy clients, rather, it is for any and everyone who needs help writing out goals.

I would like the design of the flyer to reflect the concept of organization in a unique way.

http://themindcraftstudyhouse.com/wp-content/uploads/2012/02/websitelogo2.jpg

ORGANIZATION

Write out your goals for the year.

How to organize your life in 3 easy steps.
Have fun organizing your life and plans.
Join a group of people dedicated to organizing all areas of life.
Complete your tasks in a fast, fun game format.
Walk away with your major goals broken down into their component parts and organize on a yearly calendar.
Three 3 hour days spent in making your life happier, less stressed and with realistic picture of what needs to be accomplished.
more effective in everything I do.
Being organized helps free our minds, enjoy relationships more, feel happier, and have greater meaning in life.

You will walk away with detailed plans for 2013.

COST: $600 for all three days.

WHO: Led by Maren Holtby, Cognitive Speech Therapist
WHERE: 4971 E Pruett Ave
Kennewick, WA 99336
509-218-3907

Requirements
Must have
• My logo from my website. A unique organized appearance.

```html
<!DOCTYPE html>
<html lang="en">
<head>
<meta charset="utf-8">
<title>Organization Workshop Flyer</title>
<link rel="stylesheet" href="https://fonts.googleapis.com/css2?family=Limelight&family=Arimo:ital,wght@0,400;0,700;1,700&family=Tinos:wght@700&display=swap">
<style>
  :root {
    --cream-light: #fffef6;
    --cream-warm: #fbefbd;
    --title-red: #a3172b;
    --accent-red: #b01e2c;
    --body-grey: #333333;
    --sub-grey: #555555;
    --rule-grey: #a9a59a;
    --brand-blue: #2350a8;
    --photo-light: #f6e7c6;
    --photo-mid: #e2c08e;
    --band-orange: #e8923a;
    --band-blue: #2a4f95;
  }
  * { margin: 0; padding: 0; box-sizing: border-box; }
  html, body { width: 927px; height: 1200px; overflow: hidden; }
  body { font-family: "Arimo", Arial, sans-serif; color: var(--body-grey); }

  .flyer {
    position: relative;
    width: 927px;
    height: 1200px;
    overflow: hidden;
    background: radial-gradient(ellipse at 20% 10%, var(--cream-light) 0%, #fff9de 45%, var(--cream-warm) 100%);
  }

  .flyer-title {
    position: absolute;
    left: 92px;
    top: 112px;
    font-family: "Limelight", "Times New Roman", serif;
    font-weight: 400;
    font-size: 98px;
    line-height: 1;
    color: var(--title-red);
    white-space: nowrap;
    transform: scaleX(0.53);
    transform-origin: left top;
    text-shadow: 3px 3px 4px rgba(90, 20, 20, 0.35);
  }

  .flyer-subtitle {
    position: absolute;
    left: 90px;
    top: 226px;
    font-size: 27px;
    font-weight: 700;
    font-style: italic;
    color: var(--sub-grey);
    white-space: nowrap;
  }

  .benefit-list {
    position: absolute;
    left: 80px;
    top: 340px;
    width: 440px;
    list-style: none;
    font-size: 17.5px;
    line-height: 22px;
  }
  .benefit-list li {
    position: relative;
    padding-left: 17px;
  }
  .benefit-list li::before {
    content: "";
    position: absolute;
    left: 2px;
    top: 8px;
    width: 6px;
    height: 6px;
    border-radius: 50%;
    background: var(--accent-red);
  }

  .hero-photo {
    position: absolute;
    left: 530px;
    top: 272px;
    width: 350px;
    height: 495px;
    background: linear-gradient(160deg, var(--photo-light) 0%, var(--photo-mid) 100%);
  }

  .plans-note {
    position: absolute;
    left: 95px;
    top: 716px;
    font-size: 19px;
    font-weight: 700;
    color: var(--accent-red);
  }

  .session-time {
    position: absolute;
    left: 95px;
    top: 811px;
    font-size: 19px;
    font-weight: 700;
    color: var(--accent-red);
  }

  .details {
    position: absolute;
    left: 95px;
    top: 866px;
    display: grid;
    grid-template-columns: 70px auto;
    font-size: 16px;
    line-height: 23px;
  }
  .details dt {
    font-weight: 700;
    color: var(--accent-red);
  }

  .cost {
    position: absolute;
    left: 95px;
    top: 997px;
    width: 262px;
    padding: 10px 0 11px;
    border-top: 1.5px solid var(--rule-grey);
    border-bottom: 1.5px solid var(--rule-grey);
    font-size: 14px;
    font-weight: 700;
    white-space: nowrap;
    color: var(--body-grey);
  }

  .brand {
    position: absolute;
    left: 28px;
    top: 1082px;
    display: flex;
    align-items: center;
    gap: 18px;
  }
  .brand-mark {
    width: 92px;
    height: 92px;
    border-radius: 50%;
    background: var(--brand-blue);
  }
  .brand-name {
    font-family: "Tinos", "Times New Roman", serif;
    font-weight: 700;
    font-size: 40px;
    line-height: 1;
    color: var(--brand-blue);
  }

  .website {
    position: absolute;
    right: 22px;
    top: 1146px;
    font-size: 17px;
    color: var(--body-grey);
  }
  .website .accent { color: var(--accent-red); }

  .footer-bands {
    position: absolute;
    left: 0;
    bottom: 0;
    width: 100%;
    height: 11px;
    background: linear-gradient(to bottom, var(--band-orange) 0 4px, var(--cream-light) 4px 6px, var(--band-blue) 6px 11px);
  }
</style>
</head>
<body>
<main class="flyer">
  <h1 class="flyer-title">ORGANIZATION</h1>
  <p class="flyer-subtitle">Write out your goals for the year.</p>

  <ul class="benefit-list">
    <li>How to organize your life in 3 easy steps</li>
    <li>Have fun organizing your life and plans</li>
    <li>Join a group of people dedicated to organizing all areas of life</li>
    <li>Complete your tasks in a fast, fun game format</li>
    <li>Walk away with your major goals broken down into their component parts and organize on a yearly calendar</li>
    <li>Three 3 hour days spent in making your life happier, less stressed and with realistic picture of what needs to be accomplished more effective in everything I do</li>
    <li>Being organized helps free our minds, enjoy relationships more, feel happier, and have greater meaning in life.</li>
  </ul>

  <div class="hero-photo" role="img" aria-label="Photo of a baby wearing red boxing gloves bursting out of a cracked eggshell"></div>

  <p class="plans-note">You will walk away with detailed plans for 2013.</p>
  <p class="session-time">Time: 9:00 a.m. - 12:00 p.m</p>

  <dl class="details">
    <dt>WHO</dt><dd>Led by Maren Holtby,<br>Cognitive Speech Therapist</dd>
    <dt>WHERE</dt><dd>4971 E Pruett Ave<br>Kennewick, WA 99336</dd>
    <dt>CALL</dt><dd>509.218.3907</dd>
  </dl>

  <p class="cost">COST: $600 FOR ALL THREE DAYS.</p>

  <div class="brand">
    <span class="brand-mark" aria-hidden="true"></span>
    <span class="brand-name">The Mindcraft<br>Study House</span>
  </div>

  <p class="website">www.<span class="accent">themindcraft</span>study<span class="accent">house</span>.com</p>

  <div class="footer-bands" aria-hidden="true"></div>
</main>
</body>
</html>
```